Identity Package (Logo, Website)

We need a logo and website design for a new company.
The new company is a voicemail transcription service provider. It's name is KL9BQZ.io
It will be very transactional. We like the "bootstrap" look and feel, and will be using a developer familiar with bootstrap. Here are the kinds of webpages we like :
https://www.lumenvane.io
http://www.quorbil.com/
http://www.plenivo.com/
There will only be 5 pages, as follows :
1- Homepage
2- Voicemail Transcription for Individuals
3- Voicemail Transcription for Companies
4- Wholesale Voicemail Transcription for Service Providers/Enterprises
5- Contact us
As far as the logo is concerned, we'd like to have just stylized text. It should be done in such a way as to make it easy to see the different elements of the name, which are KL, 2, and BQZ.
Reason: I have received a number of designs, but the designs are mostly from the same few designers (not that much variety in designers). I'd like a few more to compare if possible, so I thought I would keep this open until Monday to give more designers the opportunity to submit over the weekend. Thanks!

```html
<!DOCTYPE html>
<html lang="en">
<head>
<meta charset="utf-8">
<title>KL9BQZ.io — Voicemail to Text Services</title>
<link rel="stylesheet" href="https://fonts.googleapis.com/css2?family=Open+Sans:wght@400;600;700&display=swap">
<style>
  :root {
    --green: #8dc63f;
    --green-dark: #76aa2c;
    --ink: #333333;
    --muted: #666666;
    --topbar: #444444;
    --topbar-text: #aaaaaa;
    --white: #ffffff;
    --band: #f3f4f3;
    --rule: #dcdcdc;
    --dark-box: rgba(20, 20, 20, 0.85);
  }
  * { margin: 0; padding: 0; box-sizing: border-box; }
  html, body { width: 1200px; height: 1000px; overflow: hidden; }
  body { font-family: "Open Sans", Arial, sans-serif; color: var(--ink); background: var(--white); position: relative; }

  .topbar { position: absolute; left: 0; top: 0; width: 1200px; height: 28px; background: var(--topbar); border-bottom: 2px solid var(--green); }
  .topbar__contact { position: absolute; left: 172px; top: 5px; font-size: 10.5px; color: var(--topbar-text); }
  .topbar__social { position: absolute; right: 166px; top: 5px; display: flex; gap: 19px; }
  .topbar__social span { width: 15px; height: 15px; border-radius: 50%; background: #8a8a8a; display: block; }

  .header { position: absolute; left: 0; top: 28px; width: 1200px; height: 88px; background: var(--white); }
  .brand { position: absolute; left: 172px; top: 22px; font-size: 29px; font-weight: 700; color: var(--ink); letter-spacing: 0.5px; display: flex; align-items: center; gap: 8px; }
  .brand__mark { width: 12px; height: 12px; background: var(--green); border-radius: 50%; display: block; }
  .nav { position: absolute; top: 0; right: 139px; display: flex; height: 88px; }
  .nav a { display: block; padding: 0 18px; line-height: 92px; font-size: 12.5px; font-weight: 600; color: #555; text-decoration: none; position: relative; }
  .nav a.is-active { color: var(--green); padding: 0 20px; }
  .nav a.is-active::after { content: ""; position: absolute; left: 0; right: 0; bottom: 0; height: 3px; background: #3a3a3a; }

  .hero { position: absolute; left: 0; top: 116px; width: 1200px; height: 395px; overflow: hidden;
    background: radial-gradient(ellipse at 60% 45%, #b56a5a 0%, #7d6a3a 22%, transparent 50%),
                radial-gradient(ellipse at 15% 20%, #a9cc3a 0%, transparent 45%),
                linear-gradient(100deg, #6f9a22 0%, #4f6f1a 30%, #5a4a2a 55%, #4a6a20 80%, #8abb35 100%); }
  .hero__art { position: absolute; left: 200px; top: 75px; width: 335px; height: 220px; border-radius: 12px; background: rgba(141, 198, 63, 0.35); }
  .hero__title { position: absolute; left: 653px; top: 67px; width: 414px; height: 51px; background: var(--dark-box); color: var(--white); font-size: 26.5px; font-weight: 600; line-height: 51px; padding-left: 15px; white-space: nowrap; }
  .hero__lead { position: absolute; left: 658px; top: 137px; color: var(--white); font-size: 25.5px; line-height: 34px; font-weight: 400; white-space: nowrap; }
  .hero__rule { position: absolute; left: 658px; width: 409px; height: 1px; background: rgba(255,255,255,0.45); }
  .hero__note { position: absolute; left: 662px; top: 240px; font-size: 11.5px; color: var(--white); white-space: nowrap; }
  .btn-purchase { position: absolute; left: 658px; top: 301px; width: 129px; height: 35px; background: var(--green); border-bottom: 3px solid var(--green-dark); color: var(--white); font-size: 12px; font-weight: 700; text-align: center; line-height: 33px; text-decoration: none; }
  .hero__arrow { position: absolute; top: 181px; width: 31px; height: 31px; background: #1c2410; border-radius: 2px; }
  .hero__arrow svg { display: block; margin: 9px auto; }

  .features { position: absolute; left: 0; top: 573px; width: 1200px; }
  .feature { position: absolute; width: 226px; text-align: center; }
  .feature__icon { width: 70px; height: 70px; border-radius: 50%; background: var(--green); margin: 0 auto; display: flex; align-items: center; justify-content: center; }
  .feature__title { margin-top: 18px; font-size: 16px; font-weight: 400; color: var(--ink); letter-spacing: 0.3px; }
  .feature__text { margin-top: 8px; font-size: 11.6px; line-height: 19.5px; color: var(--muted); }

  .possibilities { position: absolute; left: 0; top: 816px; width: 1200px; height: 184px; background: var(--band); border-top: 2px solid var(--rule); text-align: center; }
  .possibilities__title { margin-top: 25px; font-size: 19.5px; font-weight: 400; color: var(--ink); }
  .possibilities__title strong { font-weight: 700; }
  .possibilities__text { margin-top: 7px; font-size: 11.6px; line-height: 20px; color: #555; }
  .slider-nav { position: absolute; left: 582px; top: 116px; display: flex; gap: 3px; }
  .slider-nav span { width: 25px; height: 22px; display: flex; align-items: center; justify-content: center; border-radius: 2px; }
  .slider-nav .prev { background: #c9c9c9; }
  .slider-nav .next { background: #666; }
  .possibilities__rule { position: absolute; left: 172px; top: 155px; width: 871px; height: 3px; background: var(--rule); }
  .thumb { position: absolute; top: 178px; width: 204px; height: 10px; }
</style>
</head>
<body>
  <div class="topbar">
    <div class="topbar__contact">Call Us: (1)555 014 726 - Mail hello@kl9bqz.io</div>
    <div class="topbar__social" aria-label="Social links">
      <span></span><span></span><span></span><span></span><span></span><span></span>
    </div>
  </div>

  <header class="header">
    <div class="brand"><span>KL9BQZ.io</span><span class="brand__mark"></span></div>
    <nav class="nav">
      <a href="#" class="is-active">HOME</a>
      <a href="#">FOR INDIVIDUALS</a>
      <a href="#">FOR COMPANIES</a>
      <a href="#">FOR WHOLESELLERS</a>
      <a href="#">CONTACT</a>
    </nav>
  </header>

  <section class="hero" role="img" aria-label="Blurred green garden photograph background">
    <div class="hero__art" role="img" aria-label="Illustration of a person with a speech bubble linked to mail, document and calendar icons"></div>
    <h1 class="hero__title">VOICEMAIL TO TEXT SERVICES</h1>
    <p class="hero__lead">Read Your Voicemails Anywhere,<br>Anytime on Your Mobile Phone.</p>
    <div class="hero__rule" style="top:223px"></div>
    <p class="hero__note">TEXT DELIVERY ENSURES YOU GET THE MESSAGE ANYWHERE AT ANY TIME</p>
    <div class="hero__rule" style="top:268px"></div>
    <a href="#" class="btn-purchase">PURCHASE NOW</a>
    <div class="hero__arrow" style="left:3px"><svg width="8" height="12" viewBox="0 0 8 12"><path d="M6 1 L1 6 L6 11" stroke="#fff" stroke-width="2.5" fill="none"/></svg></div>
    <div class="hero__arrow" style="left:1166px"><svg width="8" height="12" viewBox="0 0 8 12"><path d="M2 1 L7 6 L2 11" stroke="#fff" stroke-width="2.5" fill="none"/></svg></div>
  </section>

  <section class="features">
    <div class="feature" style="left:154px">
      <div class="feature__icon"><svg width="30" height="30" viewBox="0 0 30 30" fill="none" stroke="#fff" stroke-width="2.2" stroke-linejoin="round"><rect x="4" y="13" width="5" height="13"/><path d="M9 14 L14 4 Q17 4 16 9 L15 12 H24 Q26 13 25 16 L22 25 Q21 26 19 26 H9"/></svg></div>
      <h3 class="feature__title">AWESOME SUPPORT</h3>
      <p class="feature__text">Neque porro quisquam est, qui<br>dolorem ipsum quia dolor sit<br>consectetur, adipisci.</p>
    </div>
    <div class="feature" style="left:381px">
      <div class="feature__icon"><svg width="32" height="32" viewBox="0 0 32 32"><path d="M4 5 H28 V23 H19 L16 28 L13 23 H4 Z" fill="#fff"/><path d="M9 11 H23 M9 15 H23 M9 19 H19" stroke="#8dc63f" stroke-width="1.8"/></svg></div>
      <h3 class="feature__title">VOICE BIOMETRICS</h3>
      <p class="feature__text">Neque porro quisquam est, qui<br>dolorem ipsum quia dolor sit<br>consectetur, adipisci.</p>
    </div>
    <div class="feature" style="left:607px">
      <div class="feature__icon"><svg width="30" height="30" viewBox="0 0 30 30" fill="none" stroke="#fff" stroke-width="2.4"><path d="M17 6 H5 V25 H24 V13"/><path d="M12 19 L13 15 L24 4 L27 7 L16 18 Z" fill="#fff"/></svg></div>
      <h3 class="feature__title">TRANSCRIPTION</h3>
      <p class="feature__text">Neque porro quisquam est, qui<br>dolorem ipsum quia dolor sit<br>consectetur, adipisci.</p>
    </div>
    <div class="feature" style="left:835px">
      <div class="feature__icon"><svg width="34" height="34" viewBox="0 0 34 34"><path d="M5 18 L18 5 H29 V16 L16 29 Z" fill="#fff"/><circle cx="24" cy="10" r="2.2" fill="#8dc63f"/><text x="16" y="21" font-size="10" font-weight="700" fill="#8dc63f" text-anchor="middle" transform="rotate(-45 16 18)">$</text></svg></div>
      <h3 class="feature__title">AFFORDABLE PLANS</h3>
      <p class="feature__text">Neque porro quisquam est, qui<br>dolorem ipsum quia dolor sit<br>consectetur, adipisci.</p>
    </div>
  </section>

  <section class="possibilities">
    <h2 class="possibilities__title">YOUR MOBILE LIFE, <strong>COUNTLESS POSSIBILITIES</strong></h2>
    <p class="possibilities__text">Download mobile apps for life, work and play. Powerful transcription. More control. More accurate. Faster.<br>Professionally customer service with robust ideas.</p>
    <div class="slider-nav">
      <span class="prev"><svg width="7" height="11" viewBox="0 0 7 11"><path d="M5.5 1 L1.5 5.5 L5.5 10" stroke="#fff" stroke-width="2" fill="none"/></svg></span>
      <span class="next"><svg width="7" height="11" viewBox="0 0 7 11"><path d="M1.5 1 L5.5 5.5 L1.5 10" stroke="#fff" stroke-width="2" fill="none"/></svg></span>
    </div>
    <div class="possibilities__rule"></div>
    <div class="thumb" style="left:172px;background:#d8dcd8" role="img" aria-label="Photo of a person using a phone"></div>
    <div class="thumb" style="left:394px;background:#6a5a48" role="img" aria-label="Photo of an office scene"></div>
    <div class="thumb" style="left:616px;background:#c8d0d8" role="img" aria-label="Photo of a workplace"></div>
    <div class="thumb" style="left:838px;background:#d0d0cc" role="img" aria-label="Photo of a mobile device in use"></div>
  </section>
</body>
</html>
```